Regional beer Moltan-Bräu needs new labels for 33cl Beercans

We are looking for a creative and professional design for our 33cl beer can label. The can itself is all black, and the design should be mainly in yellow and black colors to stand out on the store shelf.
The size of the label should be 206 mm x 80 mm

*Details and requirements:*

1. brand identity and target group
- Our brand stands for handcrafted quality with a modern touch.
- The target group is young adults and beer connoisseurs who value unique taste and stylish design.

2. style and aesthetics:*
- The design should be modern and eye-catching, inspired by the labels of Kelvo Brauerei Hamburg.
- We prefer a minimalist style with clean lines and contrasts.

3. typography:*
- Use modern, legible fonts.
- Use freely available fonts.
- The brand name and important information should be emphasized.

4. images and graphics
- The logo can be used in its entirety or in individual parts.
- Illustrations or icons that emphasize the uniqueness of our beer are welcome.

5 *Colors:*
- Main colors are yellow and black.
- Accents in other colors are possible, but should be used sparingly.

6th *Legal requirements:*
- The label must provide space for legal information such as alcohol content, origin and barcode.

7 *Technical details
- Final files should be in AI, afdesign or PDF format with a resolution of at least 300 dpi.
- The design should be created in CMYK color model.

8th *Inspiration and references:*
- Examples of labels that we like are those of Kelvo Brauerei Hamburg. We like their clear structure and modern look.

9 *Additional information:*
- The bottling date is printed on the can or bottle afterwards.
- Special features of our beer, such as flavor or special ingredients, should be highlighted.

We look forward to your creative suggestions and hope that you will help us to design a label that perfectly represents our brand!

Target Market(s)

The target group is young adults and beer connoisseurs who value unique taste and stylish design.

Industry/Entity Type

Beverage

Colors

Requirements
Must have
• The design should be modern and eye-catching but minimalist style with clean lines and contrasts. should include the writing moltan-bräu (attachment)

```html
<!DOCTYPE html>
<html lang="de">
<head>
<meta charset="utf-8">
<title>Moltan-Bräu Helles 33cl – Label</title>
<link rel="stylesheet" href="https://fonts.googleapis.com/css2?family=Alfa+Slab+One&family=Arimo:wght@700&display=swap">
<style>
  :root {
    --backdrop: #d9d9d9;
    --can-black: #0c0c0c;
    --beer-yellow: #f2b81c;
    --label-white: #f2f2f2;
  }
  html, body {
    margin: 0;
    width: 1200px;
    height: 1200px;
    overflow: hidden;
    background: var(--backdrop);
  }
  .canvas {
    position: relative;
    width: 1200px;
    height: 1200px;
  }
  .label-front {
    position: absolute;
    left: 455px;
    top: 205px;
    width: 290px;
    height: 800px;
    background: var(--can-black);
    overflow: hidden;
  }
  .brush-swoosh {
    position: absolute;
    inset: 0;
  }
  .brand-seal {
    position: absolute;
    left: 25px;
    top: 134px;
    width: 252px;
    height: 252px;
    box-sizing: border-box;
    border-radius: 50%;
    border: 2px solid var(--label-white);
    background: var(--can-black);
    display: flex;
    align-items: center;
    justify-content: center;
  }
  .brand-name {
    font-family: "Alfa Slab One", serif;
    font-size: 22px;
    line-height: 1;
    color: var(--beer-yellow);
    white-space: nowrap;
  }
  .style-name {
    position: absolute;
    left: 0;
    right: 0;
    top: 540px;
    margin: 0;
    text-align: center;
    font-family: "Alfa Slab One", serif;
    font-weight: 400;
    font-size: 56px;
    line-height: 1;
    white-space: nowrap;
    color: var(--beer-yellow);
  }
  .style-divider {
    position: absolute;
    left: 30px;
    top: 630px;
    width: 230px;
    height: 12px;
  }
  .alcohol-content {
    position: absolute;
    left: 0;
    right: 0;
    top: 666px;
    margin: 0;
    text-align: center;
    font-family: "Arimo", sans-serif;
    font-weight: 700;
    font-size: 20px;
    line-height: 1.2;
    color: var(--label-white);
  }
  .volume {
    position: absolute;
    left: 0;
    right: 0;
    top: 698px;
    margin: 0;
    text-align: center;
    font-family: "Arimo", sans-serif;
    font-weight: 700;
    font-size: 56px;
    line-height: 1.2;
    color: var(--beer-yellow);
  }
</style>
</head>
<body>
<main class="canvas">
  <section class="label-front">
    <svg class="brush-swoosh" viewBox="0 0 290 800" width="290" height="800" role="img" aria-label="Yellow brush-stroke swoosh across the upper label">
      <path fill="var(--beer-yellow)" d="M112,0 L290,0 L290,375 C255,400 205,435 150,460 C95,475 48,430 38,365 C28,290 52,150 112,0 Z"/>
    </svg>

    <div class="brand-seal">
      <span class="brand-name">MOLTAN-BRÄU</span>
    </div>

    <h1 class="style-name">HELLES</h1>

    <svg class="style-divider" viewBox="0 0 230 12" width="230" height="12" aria-hidden="true">
      <g stroke="var(--beer-yellow)" stroke-width="1.5" fill="none">
        <line x1="6" y1="6" x2="224" y2="6"/>
        <polyline points="10,2 6,6 10,10"/>
        <polyline points="220,2 224,6 220,10"/>
      </g>
    </svg>

    <p class="alcohol-content">Alc. 4.8% vol.</p>
    <p class="volume">33cl</p>
  </section>
</main>
</body>
</html>
```